PowerPoint Design for a Biotech Consulting Firm

We need a powerpoint design for a new business based in Philadelphia called VentoraRx. This is a consulting firm that will serve medical diagnostics industry, which is part of the life science/healthcare industry focusing on developing and marketing products that help in early detection, monitoring or management of diseases. Our consulting firm will help medical diagnostic companies to overcome key challenges in designing, evaluating and marketing new products.Our company name is VentoraRx. Ventora is Latin word for "something", Dx represents diagnostics. The idea behind the name is that we help companies to transform the original, early product ideas ("nothing") into "something" which is a product with full clinical utility that will help to improve health and well-being.The powerpoint should use the visual feel of the logo (attached), be modern, simple and clean looking and represent creativity, innovation, scientific thinking and progress.

Target Market(s)

Biotech

Industry/Entity Type

Biotechnology

Font styles to use
Sans Serif

Colors
0355a3
3276b5
85abd2
cfdeed
ffffff
959595
aaaaaa
cbcbcb
070707

Requirements
Must have
• - look and feel, logo colors
• - multiple slide formats

```html
<!DOCTYPE html>
<html lang="en">
<head>
<meta charset="utf-8">
<title>VentoraRx PowerPoint Presentation Design</title>
<link rel="stylesheet" href="https://fonts.googleapis.com/css2?family=Montserrat:wght@400;500;600;700&display=swap">
<style>
:root{
  --navy:#0355a3;
  --blue:#3276b5;
  --sky:#85abd2;
  --mist:#cfdeed;
  --white:#ffffff;
  --grey:#959595;
  --grey-2:#aaaaaa;
  --grey-3:#cbcbcb;
  --ink:#070707;
  --header:#4b6e92;
  --page:#e8edf3;
}
*{box-sizing:border-box;margin:0;padding:0}
html,body{width:781px;height:1200px;overflow:hidden}
body{background:var(--page);font-family:"Montserrat",Arial,sans-serif;color:var(--ink);position:relative}
.header{position:absolute;left:0;top:0;width:781px;height:72px;background:var(--header);display:flex;align-items:center;justify-content:center}
.header h1{color:var(--white);font-weight:600;font-size:25px;letter-spacing:.2px}
.hero{position:absolute;left:0;top:72px;width:781px;height:222px;background:linear-gradient(180deg,#f3f6fa,#e2e9f1);overflow:hidden}
.slide{position:absolute;background:var(--white);overflow:hidden;box-shadow:0 1px 3px rgba(7,7,7,.14)}
.grid .slide{width:246px;height:138px}
.glow{position:absolute;width:90px;height:70px;background:radial-gradient(circle at 100% 0,var(--mist),rgba(207,222,237,0) 70%)}
.glow.tr{right:0;top:0}
.glow.bl{left:0;bottom:0;transform:rotate(180deg)}
.photo{position:absolute;background:linear-gradient(135deg,#9fb9d3,#5f83a8 55%,#c9d7e5)}
.photo.warm{background:linear-gradient(135deg,#d9e2ea,#9aaebf 60%,#e7ecf1)}
.photo.lab{background:linear-gradient(135deg,#bfd2e6,#7e9fc0 50%,#eaf0f6)}
.tag{position:absolute;top:8px;left:50%;transform:translateX(-50%);background:var(--sky);color:var(--white);font-size:8px;font-weight:600;padding:3px 10px;white-space:nowrap}
.big{position:absolute;font-weight:500;color:var(--blue);font-size:11px;line-height:1.1;white-space:nowrap}
.big b{display:block;font-size:14px;font-weight:500}
.txt{position:absolute;font-size:4.5px;line-height:1.5;color:var(--grey)}
.name{position:absolute;font-size:5px;font-weight:600;color:var(--ink);text-align:center}
.brand-panel{position:absolute;background:var(--white);display:flex;flex-direction:column;align-items:center;justify-content:center;text-align:center}
.brand-name{font-weight:600;color:var(--blue);white-space:nowrap}
.num{position:absolute;font-size:5px;font-weight:600;color:var(--blue)}
.sq{position:absolute;width:7px;height:7px;background:var(--blue)}
svg{position:absolute;overflow:visible}
</style>
</head>
<body>

<header class="header"><h1>VentoraRx PowerPoint Presentation Design</h1></header>

<section class="hero">
  <div class="slide" style="left:14px;top:52px;width:230px;height:130px;opacity:.85">
    <div class="photo lab" role="img" aria-label="Laboratory sample tubes" style="left:10px;top:40px;width:80px;height:50px"></div>
    <div class="txt" style="left:100px;top:45px;width:110px">Clinical insight for new diagnostic tools and tests.</div>
  </div>
  <div class="slide" style="left:110px;top:30px;width:240px;height:140px">
    <div class="glow tr"></div>
    <div class="photo" role="img" aria-label="Scientist at a microscope" style="left:14px;top:30px;width:95px;height:75px"></div>
    <div class="txt" style="left:120px;top:40px;width:100px">From early idea to full clinical utility.</div>
  </div>
  <div class="slide" style="left:537px;top:52px;width:230px;height:130px;opacity:.85">
    <svg width="60" height="60" style="left:150px;top:35px" viewBox="0 0 60 60"><circle cx="30" cy="30" r="24" fill="none" stroke="#cfdeed" stroke-width="7"/><circle cx="30" cy="30" r="24" fill="none" stroke="#3276b5" stroke-width="7" stroke-dasharray="113 151" transform="rotate(-90 30 30)"/></svg>
    <div class="txt" style="left:20px;top:45px;width:110px">Measured progress across every project stage.</div>
  </div>
  <div class="slide" style="left:431px;top:30px;width:240px;height:140px">
    <div class="glow tr"></div>
    <svg width="60" height="60" style="left:150px;top:40px" viewBox="0 0 60 60"><circle cx="30" cy="30" r="24" fill="none" stroke="#cfdeed" stroke-width="7"/><circle cx="30" cy="30" r="24" fill="none" stroke="#0355a3" stroke-width="7" stroke-dasharray="113 151" transform="rotate(-90 30 30)"/><text x="30" y="33" text-anchor="middle" font-family="Montserrat,sans-serif" font-size="9" font-weight="600" fill="#0355a3">75%</text></svg>
    <div class="txt" style="left:20px;top:45px;width:110px">Results that support safer, earlier detection.</div>
  </div>
  <div class="slide" style="left:215px;top:14px;width:350px;height:197px;box-shadow:0 6px 18px rgba(7,7,7,.25)">
    <div class="photo" role="img" aria-label="Medical staff walking down a hospital corridor" style="left:0;top:0;width:190px;height:197px"></div>
    <div class="glow tr" style="width:140px;height:110px"></div>
    <div class="brand-panel" style="left:140px;top:52px;width:130px;height:92px">
      <span class="brand-name" style="font-size:19px">VentoraRx</span>
    </div>
  </div>
</section>

<main class="grid">
  <div class="slide" style="left:12px;top:302px">
    <div class="photo" role="img" aria-label="Medical staff in a hospital corridor" style="left:0;top:0;width:120px;height:138px"></div>
    <div class="glow tr"></div>
    <div class="brand-panel" style="left:92px;top:36px;width:88px;height:64px">
      <span class="brand-name" style="font-size:13px">VentoraRx</span>
    </div>
  </div>
  <div class="slide" style="left:268px;top:302px">
    <div class="photo lab" role="img" aria-label="Laboratory workbench" style="left:0;top:0;width:105px;height:138px"></div>
    <div class="glow tr"></div>
    <div class="big" style="left:125px;top:18px;color:var(--ink)">Contents</div>
    <div class="sq" style="left:125px;top:40px"></div><div class="txt" style="left:137px;top:40px">Company overview</div>
    <div class="sq" style="left:125px;top:55px;background:var(--sky)"></div><div class="txt" style="left:137px;top:55px">Market challenges</div>
    <div class="sq" style="left:125px;top:70px"></div><div class="txt" style="left:137px;top:70px">Our services</div>
    <div class="sq" style="left:125px;top:85px;background:var(--sky)"></div><div class="txt" style="left:137px;top:85px">Case results</div>
    <div class="sq" style="left:125px;top:100px"></div><div class="txt" style="left:137px;top:100px">Next steps</div>
  </div>
  <div class="slide" style="left:524px;top:302px">
    <div class="glow tr"></div>
    <div class="tag" style="left:auto;right:12px;transform:none">We are</div>
    <div class="photo lab" role="img" aria-label="Researcher handling test tubes" style="left:12px;top:12px;width:80px;height:50px"></div>
    <div class="txt" style="left:12px;top:72px;width:90px">We guide diagnostic teams from concept to launch with focus.</div>
    <div class="photo" role="img" aria-label="Scientist reviewing samples" style="left:112px;top:50px;width:120px;height:76px"></div>
  </div>

  <div class="slide" style="left:12px;top:450px">
    <div class="glow tr"></div><div class="glow bl"></div>
    <div class="brand-name" style="position:absolute;left:0;width:246px;top:40px;text-align:center;font-size:18px">VentoraRx</div>
    <div class="txt" style="left:40px;top:74px;width:166px;text-align:center;background:var(--mist);padding:4px;color:var(--blue)">Turning early product ideas into tests with real clinical value.</div>
  </div>
  <div class="slide" style="left:268px;top:450px">
    <div class="glow tr"></div>
    <div class="tag">Our Team</div>
    <div class="photo warm" role="img" aria-label="Team member portrait" style="left:30px;top:34px;width:44px;height:44px"></div>
    <div class="photo warm" role="img" aria-label="Team member portrait" style="left:101px;top:34px;width:44px;height:44px"></div>
    <div class="photo warm" role="img" aria-label="Team member portrait" style="left:172px;top:34px;width:44px;height:44px"></div>
    <div class="name" style="left:20px;top:84px;width:64px">Mara Kellen</div>
    <div class="name" style="left:91px;top:84px;width:64px">Tom Reyes</div>
    <div class="name" style="left:162px;top:84px;width:64px">Ana Lowry</div>
    <div class="txt" style="left:20px;top:93px;width:64px;text-align:center">Clinical lead</div>
    <div class="txt" style="left:91px;top:93px;width:64px;text-align:center">Market strategy</div>
    <div class="txt" style="left:162px;top:93px;width:64px;text-align:center">Product design</div>
  </div>
  <div class="slide" style="left:524px;top:450px">
    <div class="glow tr"></div>
    <div class="tag">Our Services</div>
    <svg width="220" height="24" style="left:14px;top:40px" viewBox="0 0 220 24" fill="none" stroke="#3276b5" stroke-width="1.5">
      <circle cx="12" cy="10" r="7"/><line x1="17" y1="15" x2="23" y2="21"/>
      <rect x="42" y="3" width="16" height="16"/><line x1="46" y1="9" x2="54" y2="9"/><line x1="46" y1="13" x2="54" y2="13"/>
      <path d="M80 19V8h5v11M88 19V4h5v15"/>
      <circle cx="120" cy="11" r="8"/><path d="M116 11l3 3 5-6"/>
      <path d="M148 4h12l-4 8 4 8h-12z"/>
      <circle cx="196" cy="11" r="4"/><circle cx="196" cy="11" r="8"/>
    </svg>
    <div class="txt" style="left:10px;top:74px;width:228px;display:flex;justify-content:space-between"><span>Research</span><span>Planning</span><span>Analysis</span><span>Validation</span><span>Launch</span><span>Focus</span></div>
    <div class="txt" style="left:10px;top:88px;width:228px;text-align:center">Support at every step of the diagnostic product cycle.</div>
  </div>

  <div class="slide" style="left:12px;top:598px">
    <div class="glow bl"></div>
    <div class="big" style="left:14px;top:30px">Right<b>Picture Slide</b></div>
    <div class="txt" style="left:14px;top:64px;width:96px">Use this layout to pair a key message with one strong image.</div>
    <div class="photo lab" role="img" aria-label="Lab technician pipetting samples" style="left:126px;top:14px;width:108px;height:110px"></div>
  </div>
  <div class="slide" style="left:268px;top:598px">
    <div class="glow tr"></div>
    <div class="tag">Bullet Point Slide</div>
    <svg width="220" height="24" style="left:14px;top:34px" viewBox="0 0 220 24" fill="none" stroke="#3276b5" stroke-width="1.5">
      <rect x="0" y="0" width="24" height="24" fill="#cfdeed" stroke="none"/><circle cx="12" cy="12" r="6"/>
      <rect x="64" y="0" width="24" height="24" fill="#cfdeed" stroke="none"/><path d="M70 16l5-8 5 8z"/>
      <rect x="128" y="0" width="24" height="24" fill="#cfdeed" stroke="none"/><path d="M134 12h12M140 6v12"/>
      <rect x="192" y="0" width="24" height="24" fill="#cfdeed" stroke="none"/><path d="M198 14l4 4 8-10"/>
    </svg>
    <div class="txt" style="left:8px;top:64px;width:230px;display:flex;justify-content:space-around;text-align:center"><span>Clear aims<br>for every test</span><span>Evidence<br>led design</span><span>Growth<br>in new markets</span><span>Approved<br>and ready</span></div>
    <div class="txt" style="left:20px;top:96px;width:206px;text-align:center">Four pillars that shape how we support each client.</div>
  </div>
  <div class="slide" style="left:524px;top:598px">
    <div class="glow tr"></div>
    <div class="photo warm" role="img" aria-label="Hands holding a sample vial" style="left:12px;top:14px;width:108px;height:110px"></div>
    <div class="big" style="left:134px;top:30px">Left<b>Picture Slide</b></div>
    <div class="txt" style="left:134px;top:64px;width:98px">A mirrored layout for image first stories and notes.</div>
  </div>

  <div class="slide" style="left:12px;top:746px">
    <div class="glow tr"></div>
    <div class="big" style="left:14px;top:12px;color:var(--ink)">List Slide</div>
    <div class="num" style="left:14px;top:36px">Number 1</div><div class="txt" style="left:14px;top:44px;width:96px">Short point about the topic.</div>
    <div class="num" style="left:14px;top:62px">Number 2</div><div class="txt" style="left:14px;top:70px;width:96px">Short point about the topic.</div>
    <div class="num" style="left:14px;top:88px">Number 3</div><div class="txt" style="left:14px;top:96px;width:96px">Short point about the topic.</div>
    <div class="num" style="left:130px;top:36px">Number 4</div><div class="txt" style="left:130px;top:44px;width:96px">Short point about the topic.</div>
    <div class="num" style="left:130px;top:62px">Number 5</div><div class="txt" style="left:130px;top:70px;width:96px">Short point about the topic.</div>
    <div class="num" style="left:130px;top:88px">Number 6</div><div class="txt" style="left:130px;top:96px;width:96px">Short point about the topic.</div>
  </div>
  <div class="slide" style="left:268px;top:746px">
    <div class="glow tr"></div>
    <div class="big" style="left:14px;top:12px;color:var(--ink)">List Slide</div>
    <svg width="12" height="80" style="left:14px;top:38px" viewBox="0 0 12 80"><circle cx="6" cy="6" r="5" fill="#3276b5"/><circle cx="6" cy="32" r="5" fill="#85abd2"/><circle cx="6" cy="58" r="5" fill="#3276b5"/></svg>
    <svg width="12" height="80" style="left:130px;top:38px" viewBox="0 0 12 80"><circle cx="6" cy="6" r="5" fill="#85abd2"/><circle cx="6" cy="32" r="5" fill="#3276b5"/><circle cx="6" cy="58" r="5" fill="#85abd2"/></svg>
    <div class="txt" style="left:30px;top:40px;width:90px">Step one in the plan.</div>
    <div class="txt" style="left:30px;top:66px;width:90px">Step two in the plan.</div>
    <div class="txt" style="left:30px;top:92px;width:90px">Step three in the plan.</div>
    <div class="txt" style="left:146px;top:40px;width:90px">Step four in the plan.</div>
    <div class="txt" style="left:146px;top:66px;width:90px">Step five in the plan.</div>
    <div class="txt" style="left:146px;top:92px;width:90px">Step six in the plan.</div>
  </div>
  <div class="slide" style="left:524px;top:746px">
    <div class="glow tr"></div>
    <div class="big" style="left:14px;top:12px;color:var(--ink)">List Slide</div>
    <svg width="14" height="84" style="left:14px;top:36px" viewBox="0 0 14 84" fill="none" stroke="#3276b5" stroke-width="1.3"><circle cx="7" cy="7" r="6"/><rect x="1" y="29" width="12" height="12"/><path d="M1 70l6-10 6 10z"/></svg>
    <svg width="14" height="84" style="left:130px;top:36px" viewBox="0 0 14 84" fill="none" stroke="#3276b5" stroke-width="1.3"><path d="M2 8l4 4 7-9"/><circle cx="7" cy="35" r="6"/><rect x="1" y="58" width="12" height="12"/></svg>
    <div class="txt" style="left:32px;top:40px;width:88px">Define the clinical need.</div>
    <div class="txt" style="left:32px;top:68px;width:88px">Design the study plan.</div>
    <div class="txt" style="left:32px;top:96px;width:88px">Map the market path.</div>
    <div class="txt" style="left:148px;top:40px;width:88px">Check every result.</div>
    <div class="txt" style="left:148px;top:68px;width:88px">Report to partners.</div>
    <div class="txt" style="left:148px;top:96px;width:88px">Prepare the launch.</div>
  </div>

  <div class="slide" style="left:12px;top:894px">
    <div class="glow bl"></div>
    <div class="big" style="left:14px;top:30px">Two<b>Picture Slide</b></div>
    <div class="txt" style="left:14px;top:64px;width:88px">Compare two scenes side by side with a note.</div>
    <div class="photo" role="img" aria-label="Doctor reviewing a patient chart" style="left:118px;top:14px;width:56px;height:110px"></div>
    <div class="photo lab" role="img" aria-label="Microscope slide close-up" style="left:178px;top:14px;width:56px;height:110px"></div>
  </div>
  <div class="slide" style="left:268px;top:894px">
    <div class="glow tr"></div>
    <div class="photo warm" role="img" aria-label="Lab gloves holding a test kit" style="left:12px;top:14px;width:56px;height:110px"></div>
    <div class="photo" role="img" aria-label="Research team meeting" style="left:72px;top:14px;width:56px;height:110px"></div>
    <div class="big" style="left:138px;top:30px">Two<b>Picture Slide</b></div>
    <div class="txt" style="left:138px;top:64px;width:94px">A second option for paired photo content.</div>
  </div>
  <div class="slide" style="left:524px;top:894px">
    <div class="glow tr"></div>
    <div class="tag">Chart Slide</div>
    <svg width="120" height="90" style="left:14px;top:32px" viewBox="0 0 120 90">
      <line x1="0" y1="88" x2="120" y2="88" stroke="#cbcbcb" stroke-width="1"/>
      <rect x="6" y="40" width="14" height="48" fill="#3276b5"/>
      <rect x="26" y="56" width="14" height="32" fill="#85abd2"/>
      <rect x="46" y="30" width="14" height="58" fill="#3276b5"/>
      <rect x="66" y="48" width="14" height="40" fill="#85abd2"/>
      <rect x="86" y="14" width="14" height="74" fill="#0355a3"/>
    </svg>
    <div class="txt" style="left:148px;top:40px;width:86px">Growth in client projects over five quarters.</div>
    <svg width="86" height="40" style="left:148px;top:66px" viewBox="0 0 86 40"><rect x="0" y="0" width="70" height="5" fill="#cfdeed"/><rect x="0" y="0" width="52" height="5" fill="#3276b5"/><rect x="0" y="14" width="70" height="5" fill="#cfdeed"/><rect x="0" y="14" width="38" height="5" fill="#85abd2"/><rect x="0" y="28" width="70" height="5" fill="#cfdeed"/><rect x="0" y="28" width="60" height="5" fill="#0355a3"/></svg>
  </div>

  <div class="slide" style="left:12px;top:1042px">
    <div class="glow tr"></div>
    <div class="tag">Chart Slide</div>
    <svg width="220" height="60" style="left:13px;top:36px" viewBox="0 0 220 60" font-family="Montserrat,sans-serif" font-size="9" font-weight="600" text-anchor="middle">
      <circle cx="36" cy="30" r="24" fill="none" stroke="#cfdeed" stroke-width="6"/><circle cx="36" cy="30" r="24" fill="none" stroke="#0355a3" stroke-width="6" stroke-dasharray="75.4 150.8" transform="rotate(-90 36 30)"/><text x="36" y="33" fill="#0355a3">50%</text>
      <circle cx="110" cy="30" r="24" fill="none" stroke="#cfdeed" stroke-width="6"/><circle cx="110" cy="30" r="24" fill="none" stroke="#3276b5" stroke-width="6" stroke-dasharray="90.5 150.8" transform="rotate(-90 110 30)"/><text x="110" y="33" fill="#3276b5">60%</text>
      <circle cx="184" cy="30" r="24" fill="none" stroke="#cfdeed" stroke-width="6"/><circle cx="184" cy="30" r="24" fill="none" stroke="#85abd2" stroke-width="6" stroke-dasharray="113.1 150.8" transform="rotate(-90 184 30)"/><text x="184" y="33" fill="#85abd2">75%</text>
    </svg>
    <div class="txt" style="left:12px;top:104px;width:222px;display:flex;justify-content:space-around"><span>Accuracy</span><span>Speed</span><span>Adoption</span></div>
  </div>
  <div class="slide" style="left:268px;top:1042px">
    <div class="glow tr"></div>
    <div class="tag">Timeline Slide</div>
    <svg width="210" height="20" style="left:18px;top:60px" viewBox="0 0 210 20">
      <line x1="0" y1="10" x2="210" y2="10" stroke="#85abd2" stroke-width="2"/>
      <circle cx="20" cy="10" r="5" fill="#3276b5"/><circle cx="80" cy="10" r="5" fill="#0355a3"/><circle cx="140" cy="10" r="5" fill="#3276b5"/><circle cx="195" cy="10" r="5" fill="#0355a3"/>
    </svg>
    <div class="num" style="left:28px;top:40px">Step 1</div>
    <div class="num" style="left:146px;top:40px">Step 3</div>
    <div class="txt" style="left:20px;top:48px;width:60px">Idea review</div>
    <div class="txt" style="left:138px;top:48px;width:60px">Clinical trial</div>
    <div class="num" style="left:88px;top:86px">Step 2</div>
    <div class="num" style="left:202px;top:86px">Step 4</div>
    <div class="txt" style="left:80px;top:94px;width:60px">Study design</div>
    <div class="txt" style="left:196px;top:94px;width:44px">Launch</div>
  </div>
  <div class="slide" style="left:524px;top:1042px">
    <div class="glow tr"></div><div class="glow bl"></div>
    <div class="brand-panel" style="left:53px;top:30px;width:140px;height:78px">
      <span class="brand-name" style="font-size:14px">VentoraRx</span>
      <span style="font-size:7px;font-weight:600;color:var(--ink);margin-top:10px">THANK YOU</span>
    </div>
  </div>
</main>

</body>
</html>
```